CCTV Camera Product Box Design

Hello, we are looking for a new fresh design on our product box with our new logo. I have added our old designs to show what we are kind of looking for. I have added the spec sheet as well if you want to add anything to it. I also added our current box design for the KT-MRPL-275

Target Market(s)

Distribution Shelves

Industry/Entity Type

Camera

```html
<!DOCTYPE html>
<html lang="en">
<head>
<meta charset="utf-8">
<title>KT-MRPL-275 Bullet Camera Box</title>
<link href="https://fonts.googleapis.com/css2?family=Bebas+Neue&family=Michroma&family=Montserrat:wght@700&display=swap" rel="stylesheet">
<style>
  :root {
    --stage: #58565a;
    --panel-dark: #141414;
    --panel-mid: #2a2a2a;
    --accent-red: #e0141c;
    --text-light: #f4f4f4;
    --text-soft: #d6d6d6;
    --label-grey: #9a9a9a;
    --badge-grey: #7a7a7a;
    --burst-yellow: #fff200;
    --burst-gold: #d9c430;
    --gold: #d8a531;
  }
  * { margin: 0; padding: 0; box-sizing: border-box; }
  html, body { width: 1200px; height: 1200px; overflow: hidden; background: var(--stage); }
  .box-front {
    position: absolute; left: 110px; top: 384px; width: 980px; height: 533px;
    background: linear-gradient(135deg, var(--panel-mid) 0%, var(--panel-dark) 55%, #1d1d1d 100%);
    box-shadow: 0 10px 30px rgba(0,0,0,.35);
    overflow: hidden;
    font-family: "Bebas Neue", sans-serif;
    color: var(--text-light);
  }
  .edge-stripe { position: absolute; left: 0; top: 0; width: 11px; height: 100%; background: var(--accent-red); }
  .series-band {
    position: absolute; left: 11px; top: 0; right: 0; height: 34px;
    background: linear-gradient(90deg, rgba(60,60,60,0) 0%, #6f6f6f 30%, #cfcfcf 70%, #e6e6e6 100%);
  }
  .series-title {
    position: absolute; left: 538px; top: 9px;
    font-family: "Michroma", sans-serif; font-size: 14px; letter-spacing: 1px; color: #111;
  }
  .brand { position: absolute; left: 53px; top: 27px; display: flex; align-items: flex-end; gap: 8px; }
  .brand-square { width: 22px; height: 22px; background: var(--accent-red); margin-bottom: 8px; }
  .brand-name { font-family: "Montserrat", sans-serif; font-weight: 700; font-size: 34px; line-height: 1; color: var(--text-light); }
  .brand-url { font-family: "Montserrat", sans-serif; font-weight: 700; font-size: 9px; color: var(--text-light); margin-bottom: 4px; margin-left: 4px; }
  .headline { position: absolute; left: 47px; top: 108px; line-height: 1; }
  .headline .kicker { font-size: 23px; color: var(--text-soft); }
  .headline .subtitle { font-size: 30px; color: var(--text-soft); margin-top: 2px; }
  .headline .title-main { font-size: 89px; letter-spacing: -1px; margin-top: 2px; line-height: .86; }
  .headline .title-sub { font-size: 66px; line-height: .9; margin-top: 2px; }
  .headline .model { font-size: 13px; margin-top: 6px; }
  .spec-list { position: absolute; left: 47px; top: 333px; list-style: none; }
  .spec-list li { font-size: 28px; line-height: 36.3px; color: var(--text-soft); }
  .product-photo {
    position: absolute; left: 467px; top: 40px; width: 513px; height: 300px;
    background: radial-gradient(ellipse at 45% 55%, #8a8a8a 0%, #6a6a6a 40%, rgba(60,60,60,.6) 70%, rgba(30,30,30,0) 100%);
    border-radius: 45% 30% 40% 50%;
  }
  .led-burst { position: absolute; left: 779px; top: 196px; width: 140px; height: 140px; }
  .feature-row { position: absolute; left: 556px; top: 425px; display: flex; gap: 8px; }
  .feature { width: 60px; text-align: center; }
  .feature-badge {
    width: 60px; height: 60px; border-radius: 50%; background: var(--badge-grey);
    display: flex; align-items: center; justify-content: center;
    font-size: 21px; color: var(--text-light);
  }
  .feature-badge.full-hd { background: #111; flex-direction: column; line-height: .9; }
  .full-hd .hd-top { font-size: 16px; color: var(--gold); }
  .full-hd .hd-bottom { font-size: 19px; color: #111; background: var(--gold); padding: 0 3px; }
  .feature-label { font-size: 9px; color: var(--label-grey); margin-top: 11px; white-space: nowrap; }
  .cert-mark { position: absolute; left: 933px; top: 492px; width: 24px; height: 24px; border: 2px solid var(--text-light); border-radius: 50%; }
</style>
</head>
<body>
<div class="box-front">
  <div class="edge-stripe"></div>
  <div class="series-band"></div>
  <div class="series-title">SLATE LINE CAMERA SERIES</div>

  <div class="product-photo" role="img" aria-label="Grey weatherproof bullet camera with IR LED ring and wall mount bracket"></div>

  <div class="brand">
    <div class="brand-square"></div>
    <div class="brand-name">kvt</div>
    <div class="brand-url">www.keltravision.com</div>
  </div>

  <div class="headline">
    <div class="kicker">2MP 1080P AHD, HD-TVI AND 960H</div>
    <div class="subtitle">COMPOSTE COLOUR VERIFOCAL</div>
    <div class="title-main">WEATHERPROOF</div>
    <div class="title-sub">BULLET CAMERA</div>
    <div class="model">( KT-MRPL-275 )</div>
  </div>

  <ul class="spec-list">
    <li>FULL HD 1920X1080 RESOLUTION</li>
    <li>HD-TVI &amp; 1280TVL ANALOG CVBS</li>
    <li>2.8-12MM VARIFOCAL LENS</li>
    <li>DUAL VOLTAGE 12VDC / 24VAC</li>
    <li>IP 66 WEATHERPROOF RATING</li>
  </ul>

  <svg class="led-burst" viewBox="0 0 140 140" aria-label="LED lights up to 70 feet">
    <polygon fill="var(--burst-gold)" points="70,0 76,24 92,6 88,30 112,16 100,38 128,34 106,52 138,60 108,68 136,82 106,86 124,106 98,100 104,126 84,108 78,138 70,110 62,138 56,108 36,126 42,100 16,106 34,86 4,82 32,68 2,60 34,52 12,34 40,38 28,16 52,30 48,6 64,24"/>
    <circle cx="70" cy="70" r="48" fill="var(--burst-yellow)"/>
    <text x="70" y="60" text-anchor="middle" font-family="Bebas Neue, sans-serif" font-size="28" fill="#111">LED</text>
    <text x="70" y="74" text-anchor="middle" font-family="Bebas Neue, sans-serif" font-size="14" fill="#111">LIGHTS UPTO</text>
    <text x="70" y="106" text-anchor="middle" font-family="Bebas Neue, sans-serif" font-size="38" fill="#111">70FT</text>
  </svg>

  <div class="feature-row">
    <div class="feature">
      <div class="feature-badge full-hd"><span class="hd-top">Full HD</span><span class="hd-bottom">1080p</span></div>
      <div class="feature-label">FULL HD</div>
    </div>
    <div class="feature">
      <div class="feature-badge">AHD</div>
      <div class="feature-label">1080P ANALOG</div>
    </div>
    <div class="feature">
      <div class="feature-badge">HD-TVI</div>
      <div class="feature-label">1080P ANALOG</div>
    </div>
    <div class="feature">
      <div class="feature-badge">960 H</div>
      <div class="feature-label">HIGH RESOLUTION</div>
    </div>
    <div class="feature">
      <div class="feature-badge">
        <svg width="40" height="40" viewBox="0 0 40 40" aria-hidden="true">
          <circle cx="20" cy="20" r="10" fill="#fff"/>
          <g stroke="#fff" stroke-width="2" stroke-linecap="round">
            <line x1="20" y1="2" x2="20" y2="6"/><line x1="20" y1="34" x2="20" y2="38"/>
            <line x1="2" y1="20" x2="6" y2="20"/><line x1="34" y1="20" x2="38" y2="20"/>
            <line x1="7" y1="7" x2="10" y2="10"/><line x1="30" y1="30" x2="33" y2="33"/>
            <line x1="33" y1="7" x2="30" y2="10"/><line x1="7" y1="33" x2="10" y2="30"/>
          </g>
          <path d="M24 12 A10 10 0 0 1 26 28 A8 8 0 0 0 24 12Z" fill="#7a7a7a"/>
        </svg>
      </div>
      <div class="feature-label">DAY/NIGHT</div>
    </div>
  </div>

  <div class="cert-mark"></div>
</div>
</body>
</html>
```